Business card design for Luxury Real Estate

Using the corporate logo you have designed, please design a business card for a luxury real estate company in Thailand.

The brand is about elegance, calm, sophistication and luxury. The card should look clean, modern and be standard business card size. The background should be white to enable future scanning of the card (funky backgrounds result in poor card scanning results).

Text on Business Card (Front side) shall include the following:
- Corporate Logo
- Include the following business services underneath " Sales. Rentals. Investments. Financing."
- Name: Marisa Tevel
- Title: CEO, Founder
- mobile phone: +65 84219637 (Singapore), +66 7000 48261 (Thailand)
- email: marisa@goldenreedhaven.com
- skype: goldenreedhaven
- url: www.goldenreedhaven.com

Backside
- include same info but shall have Chinese name and title.

please use the attached additional language in mandarin for "sales. rentals. investments. financing."

Normal 0 false false false EN-US JA X-NONE 售和房租。投和融    

Target Market(s)

high net worth individuals, business men/ women, finance managers.

Industry/Entity Type

Real Estate

Requirements
Must have
• elegant, sophisticated, clean, modern look. appealing but comforting to the eye. should not be crowded and overcomplicated.

```html
<!DOCTYPE html>
<html lang="en">
<head>
<meta charset="utf-8">
<title>Golden Reed Haven – Business Card</title>
<link href="https://fonts.googleapis.com/css2?family=Tenor+Sans&family=Noto+Sans+SC:wght@400;500&display=swap" rel="stylesheet">
<style>
  :root {
    --stage: #ecebe8;
    --card: #ffffff;
    --ink: #3a3a3a;
    --ink-soft: #5a5a5a;
    --gold: #c9a75a;
    --gold-band: #d2b06a;
    --gold-band-dark: #bf9c52;
    --grey-band-top: #f2f2f2;
    --grey-band-bottom: #8f8f8f;
    --band-text: #ffffff;
  }
  * { margin: 0; padding: 0; box-sizing: border-box; }
  html, body {
    width: 1200px; height: 901px; overflow: hidden;
    background: var(--stage);
    font-family: "Tenor Sans", sans-serif;
    color: var(--ink);
  }
  .stage {
    width: 1200px; height: 901px;
    display: flex; flex-direction: column;
    align-items: center; justify-content: center;
    gap: 40px;
  }
  .card {
    position: relative;
    width: 700px; height: 400px;
    background: var(--card);
    border-radius: 22px;
    overflow: hidden;
    box-shadow: 0 6px 22px rgba(0,0,0,.12);
  }
  .brand-name {
    position: absolute;
    left: 70px; top: 70px;
    font-family: "Tenor Sans", sans-serif;
    font-size: 40px;
    letter-spacing: .5px;
    color: var(--ink-soft);
  }
  .person {
    position: absolute;
    left: 52px; top: 190px;
  }
  .person-name {
    font-size: 26px;
    color: var(--gold);
    line-height: 1.1;
  }
  .person-title {
    font-size: 15px;
    color: var(--ink);
    margin-top: 4px;
  }
  .contacts {
    list-style: none;
    margin-top: 18px;
  }
  .contacts li {
    display: flex; align-items: center; gap: 10px;
    font-size: 15px; line-height: 22px;
    color: var(--ink);
  }
  .contacts svg { width: 14px; height: 14px; flex: none; }
  .online {
    position: absolute;
    right: 48px; top: 226px;
    list-style: none;
  }
  .online li {
    display: flex; align-items: center; gap: 10px;
    font-size: 15px; line-height: 22px;
    color: var(--ink);
  }
  .online svg { width: 14px; height: 14px; flex: none; }
  .services-band {
    position: absolute;
    left: 0; right: 0; bottom: 0;
    height: 70px;
    display: flex; align-items: center; justify-content: center;
    background: linear-gradient(180deg, var(--grey-band-top) 0%, #cfcfcf 45%, var(--grey-band-bottom) 100%);
    color: var(--band-text);
    font-size: 17px;
    letter-spacing: 6px;
  }
  .services-band.gold {
    height: 62px;
    background: linear-gradient(180deg, var(--gold-band) 0%, var(--gold-band-dark) 100%);
    color: var(--ink);
    font-family: "Noto Sans SC", sans-serif;
    font-size: 16px;
    letter-spacing: 3px;
  }
  .zh { font-family: "Noto Sans SC", sans-serif; }
</style>
</head>
<body>
<main class="stage">

  <section class="card card-front" aria-label="Business card front">
    <div class="brand-name">Golden Reed Haven</div>

    <div class="person">
      <div class="person-name">Marisa Tevel</div>
      <div class="person-title">CEO, Founder</div>
      <ul class="contacts">
        <li><svg viewBox="0 0 14 14"><rect x="1" y="3" width="12" height="8" rx="1" fill="var(--gold)"/><path d="M1.5 3.5 7 8l5.5-4.5" stroke="#fff" stroke-width="1" fill="none"/></svg>marisa@goldenreedhaven.com</li>
        <li><svg viewBox="0 0 14 14"><rect x="3.5" y="1" width="7" height="12" rx="1.3" fill="none" stroke="var(--gold)" stroke-width="1.5"/><circle cx="7" cy="11" r=".8" fill="var(--gold)"/></svg>+65 8421 9637 (Singapore)</li>
        <li><svg viewBox="0 0 14 14"><rect x="3.5" y="1" width="7" height="12" rx="1.3" fill="none" stroke="var(--gold)" stroke-width="1.5"/><circle cx="7" cy="11" r=".8" fill="var(--gold)"/></svg>+66 7000 48261 (Thailand)</li>
      </ul>
    </div>

    <ul class="online">
      <li><svg viewBox="0 0 14 14"><circle cx="7" cy="7" r="6" fill="var(--gold)"/></svg>goldenreedhaven</li>
      <li><svg viewBox="0 0 14 14"><circle cx="7" cy="7" r="5.5" fill="none" stroke="var(--gold)" stroke-width="1.3"/><ellipse cx="7" cy="7" rx="2.4" ry="5.5" fill="none" stroke="var(--gold)" stroke-width="1"/><path d="M1.5 7h11" stroke="var(--gold)" stroke-width="1"/></svg>www.goldenreedhaven.com</li>
    </ul>

    <div class="services-band">SALES • RENTALS • INVESTMENTS • FINANCING</div>
  </section>

  <section class="card card-back" aria-label="Business card back">
    <div class="brand-name">Golden Reed Haven</div>

    <div class="person">
      <div class="person-name zh">戴美莎</div>
      <div class="person-title zh">总裁</div>
      <ul class="contacts">
        <li><svg viewBox="0 0 14 14"><rect x="1" y="3" width="12" height="8" rx="1" fill="var(--gold)"/><path d="M1.5 3.5 7 8l5.5-4.5" stroke="#fff" stroke-width="1" fill="none"/></svg>marisa@goldenreedhaven.com</li>
        <li><svg viewBox="0 0 14 14"><rect x="3.5" y="1" width="7" height="12" rx="1.3" fill="none" stroke="var(--gold)" stroke-width="1.5"/><circle cx="7" cy="11" r=".8" fill="var(--gold)"/></svg>+65 8421 9637 (Singapore)</li>
        <li><svg viewBox="0 0 14 14"><rect x="3.5" y="1" width="7" height="12" rx="1.3" fill="none" stroke="var(--gold)" stroke-width="1.5"/><circle cx="7" cy="11" r=".8" fill="var(--gold)"/></svg>+66 7000 48261 (Thailand)</li>
      </ul>
    </div>

    <ul class="online">
      <li><svg viewBox="0 0 14 14"><circle cx="7" cy="7" r="6" fill="var(--gold)"/></svg>goldenreedhaven</li>
      <li><svg viewBox="0 0 14 14"><circle cx="7" cy="7" r="5.5" fill="none" stroke="var(--gold)" stroke-width="1.3"/><ellipse cx="7" cy="7" rx="2.4" ry="5.5" fill="none" stroke="var(--gold)" stroke-width="1"/><path d="M1.5 7h11" stroke="var(--gold)" stroke-width="1"/></svg>www.goldenreedhaven.com</li>
    </ul>

    <div class="services-band gold">销售和房租。投资和融资服务。</div>
  </section>

</main>
</body>
</html>
```